Vehicle van signage design nomad tank helpers business

Require a vehicle signage design that will be used to wrap a van.

I specialise in removal of fuel from people when they have filled their car with the incorrect fuel. Also in addition i provide services for contaminated fuel removal, out of fuel assist and stale fuel removal. I have a logo design already and web site done and require signage design for the van. The signage design must have the following

My logo - uploaded in files in colour and grey scale
Contact number - 0439582164
Web site link - www.nomadtankhelpers.com.au
Text - 24/7 Road side assist
Text - Filled your vehicle with the wrong fuel?

Van photos provided in files on the project portfolio with the side, front and rear view.

If further assistance is required I am happy to help and provide more input.

Target Market(s)

Customers requiring road side assist when filled vehicle with wrong fuel

Industry/Entity Type

Business

Requirements
Must have
• My logo - uploaded in files in colour and grey scale
• Contact number - 0439582164
• Web site link - www.nomadtankhelpers.com.au
• Text - 24/7 Road side assist
• Text - Filled your vehicle with the wrong fuel?

```html
<!DOCTYPE html>
<html lang="en">
<head>
<meta charset="utf-8">
<title>Nomad Tank Helpers – Van Signage</title>
<link href="https://fonts.googleapis.com/css2?family=Oswald:wght@500;600&family=Roboto:ital,wght@1,300;1,400&family=Montserrat:wght@700&display=swap" rel="stylesheet">
<style>
  :root{
    --stage:#737477;
    --blue:#0a7ccc;
    --blue-deep:#0a5fb0;
    --orange:#f26a0f;
    --white:#ffffff;
    --ink:#2b2b2b;
    --strip:#3a3a3b;
    --label:#ffffff;
  }
  *{margin:0;padding:0;box-sizing:border-box}
  html,body{width:916px;height:1200px;overflow:hidden;background:var(--stage)}
  .canvas{position:relative;width:916px;height:1200px}
  .view-label{position:absolute;font-family:"Roboto",sans-serif;font-style:italic;font-weight:300;font-size:40px;color:var(--label);transform:translateX(-50%);white-space:nowrap;line-height:1}
  .panel{position:absolute;overflow:hidden;background:var(--white)}
  .panel svg.bg{position:absolute;inset:0}
  .headline{position:absolute;font-family:"Oswald",sans-serif;font-weight:600;line-height:1.25;font-size:18px;white-space:nowrap}
  .headline .accent{color:var(--orange)}
  .headline .plain{color:var(--white)}
  .call{position:absolute;font-family:"Oswald",sans-serif;font-weight:600;white-space:nowrap}
  .call .label{display:block;color:var(--orange);font-size:16px;line-height:1.1}
  .call .phone{display:flex;align-items:center;gap:5px;color:var(--white);font-size:22px;line-height:1.15}
  .call .phone svg{flex:none}
  .brand{position:absolute;display:flex;flex-direction:column;align-items:center;transform:translateX(-50%)}
  .brand .mark{border-radius:50%;background:var(--blue)}
  .brand .name{font-family:"Montserrat",sans-serif;font-weight:700;color:var(--ink);text-align:center;line-height:1.05;letter-spacing:.5px;margin-top:8px;white-space:nowrap}
  .assist{position:absolute;display:flex;align-items:center;gap:5px;font-family:"Oswald",sans-serif;font-weight:600;white-space:nowrap}
  .assist .dot{flex:none;width:26px;height:26px;border-radius:50%;border:3px solid var(--orange)}
  .assist .hours{display:block;color:var(--blue);font-size:22px;line-height:1}
  .assist .service{display:block;color:var(--orange);font-size:11px;line-height:1.1}
  .back .assist .hours{color:var(--white)}
  .url{position:absolute;font-family:"Montserrat",sans-serif;font-weight:700;font-size:11px;letter-spacing:2px;color:var(--ink);white-space:nowrap;transform:translateX(-50%)}
  .footer-note{position:absolute;left:443px;top:1146px;transform:translateX(-50%);font-family:"Roboto",sans-serif;font-style:italic;font-weight:300;font-size:26px;color:var(--white);white-space:nowrap}
  .back .brand .name{color:var(--white)}
  .back .brand .mark{background:var(--white);border:4px solid var(--orange)}
  .url-strip{position:absolute;left:503px;top:1050px;width:288px;height:27px;background:var(--strip);display:flex;align-items:center;justify-content:center;font-family:"Montserrat",sans-serif;font-weight:700;font-size:9px;letter-spacing:1px;color:var(--orange)}
</style>
</head>
<body>
<div class="canvas">

  <div class="view-label" style="left:464px;top:32px">right side</div>
  <section class="panel side-right" style="left:120px;top:93px;width:677px;height:240px">
    <svg class="bg" width="677" height="240" viewBox="0 0 677 240" aria-hidden="true">
      <defs>
        <radialGradient id="blueR" cx="35%" cy="45%" r="70%">
          <stop offset="0" stop-color="#1a8fe0"/><stop offset="1" stop-color="#0a62b5"/>
        </radialGradient>
      </defs>
      <path d="M0 0H218C168 60 178 170 292 240H0Z" fill="url(#blueR)"/>
      <path d="M238 0C180 50 186 172 300 240" fill="none" stroke="var(--orange)" stroke-width="7"/>
      <path d="M260 240C226 222 212 200 205 170" fill="none" stroke="var(--blue)" stroke-width="5"/>
    </svg>
    <div class="headline" style="left:30px;top:40px"><span class="accent">Filled your vehicle</span><br><span class="plain">with the wrong fuel?</span></div>
    <div class="call" style="left:35px;top:110px"><span class="label">CALL US</span>
      <span class="phone"><svg width="16" height="16" viewBox="0 0 16 16" aria-hidden="true"><circle cx="8" cy="8" r="8" fill="var(--orange)"/><path d="M5 4l2 2-1 1c.6 1.3 1.7 2.4 3 3l1-1 2 2-1.5 1.3C7 11.5 4.5 9 3.8 5.5Z" fill="var(--white)"/></svg>043 958 2164</span></div>
    <div class="brand" style="left:318px;top:28px">
      <div class="mark" style="width:84px;height:84px"></div>
      <div class="name" style="font-size:18px">NOMAD TANK<br>HELPERS</div>
    </div>
    <div class="assist" style="left:446px;top:124px">
      <span class="dot"></span>
      <span><span class="hours">24/7</span><span class="service">Road side assist</span></span>
    </div>
    <div class="url" style="left:354px;top:214px">WWW.NOMADTANKHELPERS.COM.AU</div>
  </section>

  <div class="view-label" style="left:464px;top:378px">left side</div>
  <section class="panel side-left" style="left:120px;top:442px;width:677px;height:240px">
    <svg class="bg" width="677" height="240" viewBox="0 0 677 240" aria-hidden="true">
      <defs>
        <radialGradient id="blueL" cx="65%" cy="45%" r="70%">
          <stop offset="0" stop-color="#1a8fe0"/><stop offset="1" stop-color="#0a62b5"/>
        </radialGradient>
      </defs>
      <path d="M677 0H462C520 60 510 170 396 240H677Z" fill="url(#blueL)"/>
      <path d="M432 0C494 50 498 172 388 240" fill="none" stroke="var(--orange)" stroke-width="7"/>
      <path d="M420 240C452 222 466 200 474 170" fill="none" stroke="var(--blue)" stroke-width="5"/>
    </svg>
    <div class="headline" style="left:504px;top:40px"><span class="accent">Filled your vehicle</span><br><span class="plain">with the wrong fuel?</span></div>
    <div class="call" style="left:515px;top:110px"><span class="label">CALL US</span>
      <span class="phone"><svg width="16" height="16" viewBox="0 0 16 16" aria-hidden="true"><circle cx="8" cy="8" r="8" fill="var(--orange)"/><path d="M5 4l2 2-1 1c.6 1.3 1.7 2.4 3 3l1-1 2 2-1.5 1.3C7 11.5 4.5 9 3.8 5.5Z" fill="var(--white)"/></svg>043 958 2164</span></div>
    <div class="brand" style="left:361px;top:28px">
      <div class="mark" style="width:84px;height:84px"></div>
      <div class="name" style="font-size:18px">NOMAD TANK<br>HELPERS</div>
    </div>
    <div class="assist" style="left:166px;top:122px">
      <span class="dot"></span>
      <span><span class="hours">24/7</span><span class="service">Road side assist</span></span>
    </div>
    <div class="url" style="left:322px;top:214px">WWW.NOMADTANKHELPERS.COM.AU</div>
  </section>

  <div class="view-label" style="left:267px;top:718px">front side</div>
  <section class="panel front" style="left:121px;top:785px;width:287px;height:275px">
    <div class="brand" style="left:143px;top:76px">
      <div class="mark" style="width:78px;height:78px"></div>
      <div class="name" style="font-size:15px">NOMAD TANK<br>HELPERS</div>
    </div>
  </section>

  <div class="view-label" style="left:638px;top:718px">back side</div>
  <section class="panel back" style="left:503px;top:768px;width:288px;height:275px;background:var(--blue)">
    <div class="brand" style="left:140px;top:18px">
      <div class="mark" style="width:100px;height:100px"></div>
      <div class="name" style="font-size:17px">NOMAD TANK<br>HELPERS</div>
    </div>
    <div class="headline" style="left:20px;top:190px;font-size:14px"><span class="plain">Filled your vehicle<br>with the wrong fuel?</span></div>
    <div class="call" style="left:150px;top:190px"><span class="label" style="font-size:13px">CALL US</span>
      <span class="phone" style="font-size:19px"><svg width="13" height="13" viewBox="0 0 16 16" aria-hidden="true"><circle cx="8" cy="8" r="8" fill="var(--orange)"/><path d="M5 4l2 2-1 1c.6 1.3 1.7 2.4 3 3l1-1 2 2-1.5 1.3C7 11.5 4.5 9 3.8 5.5Z" fill="var(--white)"/></svg>043 958 2164</span></div>
    <div class="assist" style="left:196px;top:238px;gap:4px">
      <span class="dot" style="width:18px;height:18px;border-width:2px"></span>
      <span><span class="hours" style="font-size:14px">24/7</span><span class="service" style="font-size:8px">Road side assist</span></span>
    </div>
  </section>
  <div class="url-strip">WWW.NOMADTANKHELPERS.COM.AU</div>

  <div class="footer-note">this file image ready to print n cut ,scale 1: 20</div>
</div>
</body>
</html>
```